TRIVEX-PRO Web Design

We are a Health, Safety, Environmental & Quality Recruitment Agency, our clients are major corporate Mining, Oil & Gas and Engineering companies. We have offices in Perth & Melbourne, Australia

The website should be very functional & easy to navigate

BUT REALLY LOOKING FOR WOW FACTOR!
Updates

Please Note: TRIVEX HOLDINGS IS OUR OLD COMPANY THE NEW ONE IS "TRIVEX-PRO" 

Some idea's from our competitors:

http://www.guardlinemerit.com.au/
http://www.wardenplacement.com.au/
http://www.keelhunt.com.au/
http://www.brqstaffing.co.uk/
http://www.laborvane.com/health-safety-environment-jobs

Would love to see some of our valued clients and there logos

still looking for wow factor

Industry/Entity Type

Mining

Requirements
Must have
• A place where candidates can upload there resumes & other contact details
• eg: http://www.guardlinemerit.com.au/candidates/register-your-resume/
• A place we can load jobs on to eg: http://www.guardlinemerit.com.au/vacancies/
• Contact details:
• Perth: 17 Brindlecombe Ave, West Perth, Western Australia 6005
• t: 08 9517 3064 | f: 08 9517 3070 |
• Melbourne: Level 1, 212 Harrowgate Street, Melbourne, Victoria 3000
• t: 03 9655 4217| f: 03 9655 4290 |
• e: dmorl@trivexpro.com.au | w: http://www.trivexpro.com.au

```html
<!DOCTYPE html>
<html lang="en">
<head>
<meta charset="utf-8">
<title>TRIVEX-PRO | Health, Safety, Environmental &amp; Quality Recruitment</title>
<link href="https://fonts.googleapis.com/css2?family=Kaushan+Script&family=Signika:wght@400;600;700&family=PT+Sans:wght@400;700&display=swap" rel="stylesheet">
<style>
:root{
  --blue:#1a74bb;
  --blue-light:#2fa4e0;
  --ink:#2b2b2b;
  --text:#4a4a4a;
  --muted:#8a8a8a;
  --pill:#ececec;
  --rule:#e2e2e2;
  --navy:#0b1a33;
  --navy-field:#1b2c4a;
  --foot-text:#9aa6b8;
  --red:#e0174e;
  --orange:#f39a1e;
  --cyan:#39b4e6;
  --lime:#a8c83a;
  --white:#ffffff;
}
*{margin:0;padding:0;box-sizing:border-box}
html,body{width:1200px;height:2396px;overflow:hidden}
body{position:relative;background:var(--white);font-family:"PT Sans",Arial,sans-serif;color:var(--text);font-size:15px;line-height:22px}
.abs{position:absolute}
a{color:var(--blue);text-decoration:none}
.script{font-family:"Kaushan Script",cursive;color:var(--ink);font-weight:400}

/* header */
.site-header{position:absolute;left:0;top:0;width:1200px;height:106px;background:linear-gradient(#ffffff,#f1f1f1);border-bottom:1px solid #ddd;z-index:3}
.brand{position:absolute;left:160px;top:24px;display:flex;align-items:center;gap:12px}
.brand-mark{width:44px;height:44px;background:var(--blue);border-radius:4px}
.brand-name{font-family:"Signika",sans-serif;font-weight:600;font-size:30px;color:var(--blue);letter-spacing:1px}
.top-contact{position:absolute;top:8px;left:540px;font-size:13px;color:#666;display:flex;gap:26px;align-items:center}
.top-contact span{display:flex;align-items:center;gap:6px}
.login-tab{position:absolute;left:898px;top:0;width:132px;height:30px;background:var(--blue);border-radius:0 0 14px 14px;color:#fff;font-size:14px;text-align:center;line-height:28px;font-weight:700}
.main-nav{position:absolute;top:52px;left:492px;display:flex;gap:6px;font-size:16px}
.main-nav a{color:#333;padding:0 14px;height:30px;line-height:30px;border-radius:15px}
.main-nav a.active{background:var(--blue);color:#fff;font-weight:700}

/* hero */
.hero{position:absolute;left:0;top:106px;width:1200px;height:640px;
  background:linear-gradient(180deg,#3a2a26 0%,#a2502a 18%,#e08a3a 32%,#c8622a 46%,#4a2e26 60%,#6a4030 74%,#c9a890 90%,#ffffff 100%)}
.hero-arrow{position:absolute;top:150px}
.feature{position:absolute;top:408px;width:230px;text-align:center}
.feature-photo{width:224px;height:224px;border-radius:50%;margin:0 auto;border:6px solid #d9d4cf;box-shadow:0 4px 10px rgba(0,0,0,.35)}
.feature h2{font-size:32px;line-height:40px;margin-top:30px}
.feature p{margin-top:8px;font-size:14px;line-height:19px;color:var(--text)}
.feature a{display:block;margin-top:14px;font-size:14px}

.rule{position:absolute;left:160px;width:882px;height:1px;background:var(--rule)}

/* welcome */
.welcome-small{left:160px;top:858px;font-size:24px}
.welcome-big{left:160px;top:882px;font-family:"Signika",sans-serif;font-weight:700;font-size:46px;color:var(--blue);line-height:54px}
.pill-list{list-style:none;position:absolute;width:234px}
.pill-list li{height:30px;line-height:30px;background:var(--pill);border-radius:15px;margin-bottom:5px;padding-left:30px;font-size:14px;color:#444;position:relative}
.pill-list li::before{content:"";position:absolute;left:10px;top:10px;width:10px;height:10px;border:1.5px solid #999;border-radius:50%}
.welcome-text{left:482px;top:866px;width:560px;font-size:14px;line-height:21px}
.welcome-text p+p{margin-top:21px}

/* options */
.section-title{font-family:"Signika",sans-serif;font-weight:600;font-size:32px;color:var(--blue);line-height:40px}
.sub-title{font-family:"Signika",sans-serif;font-weight:600;font-size:19px;color:#333;letter-spacing:1px;display:flex;align-items:center;gap:10px}
.select{position:absolute;left:806px;width:236px;height:30px;border:1px solid #ddd;border-radius:15px;background:linear-gradient(#fff,#efefef);font-size:13px;color:#444;padding-left:14px;line-height:28px}
.select::after{content:"";position:absolute;right:12px;top:12px;border-left:5px solid transparent;border-right:5px solid transparent;border-top:6px solid #666}
.btn{position:absolute;height:34px;border-radius:17px;color:#fff;font-size:14px;font-weight:700;text-align:center;line-height:34px}
.btn-dark{background:linear-gradient(#3a3a3a,#111)}
.btn-blue{background:linear-gradient(#4cc0f0,#1a8fd0)}

/* posts */
.meta{font-size:12px;color:var(--muted);display:flex;gap:28px;align-items:center}
.meta span{display:flex;align-items:center;gap:6px}
.post{position:absolute;width:230px;font-size:13px;line-height:19px}
.thumb{position:absolute;width:62px;height:62px}
.thumb-news{background:linear-gradient(135deg,#8a6a3a,#d6a85a 55%,#5a4a3a)}
.thumb-client{background:linear-gradient(135deg,#e8e2dc,#b8aea6);border:2px solid #ddd}

/* footer */
.site-footer{position:absolute;left:0;top:1866px;width:1200px;height:464px;background:var(--navy);color:var(--foot-text);font-size:13px;line-height:20px}
.office{position:absolute;width:240px}
.office h3{font-family:"Signika",sans-serif;font-weight:700;font-size:16px;color:#fff;letter-spacing:.5px}
.office h3 em{font-family:"Kaushan Script",cursive;font-style:normal;font-weight:400;font-size:14px;color:#ccc}
.office .bar{height:3px;margin:6px 0 10px}
.office p+p{margin-top:20px}
.foot-title{position:absolute;left:806px;font-family:"Signika",sans-serif;font-weight:600;font-size:17px;color:#fff;letter-spacing:1px}
.email-field{position:absolute;left:806px;top:2004px;width:236px;height:30px;border-radius:15px;background:var(--navy-field);color:#ccd;font-size:13px;line-height:30px;padding-left:18px}
.social{position:absolute;left:806px;top:2140px;display:flex;gap:8px}
.social span{width:30px;height:30px;border-radius:3px}
.copy-bar{position:absolute;left:0;top:2330px;width:1200px;height:66px;background:#fff;text-align:center;font-size:13px;color:#444;line-height:66px;padding-top:6px}
.to-top{position:absolute;left:584px;top:2310px;width:32px;height:32px;border-radius:50%;background:#fff;border:2px solid #ddd}
</style>
</head>
<body>

<header class="site-header">
  <div class="brand"><span class="brand-mark"></span><span class="brand-name">TRIVEX-PRO</span></div>
  <div class="top-contact">
    <span><svg width="14" height="14" viewBox="0 0 14 14"><path d="M3 1l2 3-1.5 1.5a8 8 0 0 0 5 5L10 9l3 2-1 2c-6 0-11-5-11-11z" fill="#888"/></svg>+61 (08) 9517 3064</span>
    <span><svg width="16" height="12" viewBox="0 0 16 12"><rect x=".5" y=".5" width="15" height="11" fill="none" stroke="#888"/><path d="M1 1l7 6 7-6" fill="none" stroke="#888"/></svg>dmorl@trivexpro.com.au</span>
  </div>
  <div class="login-tab">Login | Register</div>
  <nav class="main-nav">
    <a class="active">Home</a><a>Job seekers</a><a>Employers</a><a>About us</a><a>News</a><a>Contact</a>
  </nav>
</header>

<section class="hero" role="img" aria-label="Oil and gas refinery lit at sunset reflected in water">
  <svg class="hero-arrow" style="left:92px" width="30" height="60" viewBox="0 0 30 60"><path d="M26 2L4 30l22 28" fill="none" stroke="rgba(255,255,255,.7)" stroke-width="3"/></svg>
  <svg class="hero-arrow" style="left:1078px" width="30" height="60" viewBox="0 0 30 60"><path d="M4 2l22 28L4 58" fill="none" stroke="rgba(255,255,255,.7)" stroke-width="3"/></svg>
</section>

<div class="feature" style="left:161px">
  <div class="feature-photo" role="img" aria-label="Two business people for employers" style="background:radial-gradient(circle at 50% 40%,#dcdcdc,#6a6e76)"></div>
  <h2 class="script">Employers</h2>
  <p>This is the studio's version of Lorem Ipsum. Proin gravida nibh vel velit.</p>
  <a>Click Here »</a>
</div>
<div class="feature" style="left:485px">
  <div class="feature-photo" role="img" aria-label="Candidate seated at a desk" style="background:radial-gradient(circle at 50% 40%,#f0ece6,#8a8680)"></div>
  <h2 class="script">Candidates</h2>
  <p>This is the studio's version of Lorem Ipsum. Proin gravida nibh vel velit.</p>
  <a>Register Here »</a>
</div>
<div class="feature" style="left:813px">
  <div class="feature-photo" role="img" aria-label="Site workers in hard hats for vacancies" style="background:radial-gradient(circle at 50% 40%,#e8eef4,#5a6a80)"></div>
  <h2 class="script">Vacancies</h2>
  <p>This is the studio's version of Lorem Ipsum. Proin gravida nibh vel velit.</p>
  <a>Click Here »</a>
</div>

<div class="rule" style="top:828px"></div>

<div class="abs script welcome-small">Welcome to</div>
<h1 class="abs welcome-big">TRIVEX-PRO</h1>
<svg class="abs" style="left:428px;top:866px" width="26" height="72" viewBox="0 0 26 72"><path d="M2 2l20 34L2 70" fill="none" stroke="#ddd" stroke-width="3"/></svg>
<ul class="pill-list" style="left:160px;top:950px">
  <li>Health Agency</li><li>Safety Agency</li><li>Environmental Agency</li><li>Quality Recruitment Agency</li>
</ul>
<div class="abs welcome-text">
  <p>This is the studio's version of Lorem Ipsum. Proin gravida nibh vel velit auctor aliquet. Aenean sollicitudin, lorem quis bibendum auctor, nisi elit consequat ipsum, nec sagittis elit. Duis sed odio sit amet nibh vulputate cursus a sit amet auris. Morbi accumsan ipsum velit.</p>
  <p>Nam nec tellus a odio tincidunt auctor a ornare odio. Sed non mauris vitae erat consequ auctor eu in elit. Class aptent taciti sociosqu ad litora torquent per conubia nostra, per inceptos himenaeos. Mauris in erat justo. Nullam ac urna eu felis dapibus condimentum amet a augue. Sed non neque elit. Sed ut imperdiet nisi. Proin condimentum fermentum nunc. Etiam pharetra, erat sed fermentum feugiat, velit mauris egestas quam.</p>
</div>

<div class="rule" style="top:1124px"></div>

<h2 class="abs section-title" style="left:160px;top:1158px">EMPLOYERS</h2>
<h2 class="abs section-title" style="left:482px;top:1158px"><span class="script" style="font-size:30px">Job</span> SEEKERS</h2>
<div style="position:absolute;left:438px;top:1160px;width:1px;height:340px;background:var(--rule)"></div>

<div class="abs sub-title" style="left:160px;top:1230px">QUICK OPTIONS <svg width="22" height="16" viewBox="0 0 22 16"><path d="M1 8l20-7-6 14-4-5z" fill="none" stroke="#bbb" stroke-width="1.5"/></svg></div>
<div class="abs sub-title" style="left:482px;top:1230px">QUICK OPTIONS <svg width="22" height="16" viewBox="0 0 22 16"><path d="M1 8l20-7-6 14-4-5z" fill="none" stroke="#bbb" stroke-width="1.5"/></svg></div>
<div class="abs sub-title" style="left:806px;top:1230px">QUICK SEARCH <svg width="18" height="18" viewBox="0 0 18 18"><circle cx="7" cy="7" r="5.5" fill="none" stroke="#bbb" stroke-width="2"/><path d="M11 11l6 6" stroke="#bbb" stroke-width="2"/></svg></div>

<ul class="pill-list" style="left:160px;top:1276px">
  <li>Register a Job</li><li>Our Recruitment Services</li><li>Employers Testimonials</li><li>Get In Touch</li>
</ul>
<ul class="pill-list" style="left:482px;top:1276px">
  <li>Register Your CV</li><li>Job Seekers Testimonials</li><li>Get In Touch</li>
</ul>

<div class="select" style="top:1276px">Sector</div>
<div class="select" style="top:1318px">Employment Area</div>
<div class="select" style="top:1362px">Contract/Permanent</div>
<div class="select" style="top:1404px">Salary/Pay Rate</div>
<div class="abs" style="left:806px;top:1440px;width:236px;text-align:center;font-size:12px;color:var(--muted)">Please select your criteria</div>
<div class="btn btn-dark" style="left:806px;top:1466px;width:114px">VIEW JOB</div>
<div class="btn btn-blue" style="left:928px;top:1466px;width:114px">ADVANCED</div>

<div class="rule" style="top:1538px"></div>

<h2 class="abs section-title" style="left:160px;top:1570px"><span class="script" style="font-size:30px">Featured</span> BLOG</h2>
<h2 class="abs section-title" style="left:482px;top:1570px"><span class="script" style="font-size:30px">News</span> FEED</h2>
<h2 class="abs section-title" style="left:806px;top:1570px"><span class="script" style="font-size:30px">Client's</span> SPEAK</h2>

<div class="post" style="left:160px;top:1628px">
  <div class="meta"><span><svg width="14" height="14" viewBox="0 0 14 14"><rect x="1" y="2" width="12" height="11" fill="none" stroke="#aaa"/><path d="M1 5h12" stroke="#aaa"/></svg>15 Nov, 2012</span><span><svg width="14" height="12" viewBox="0 0 14 12"><path d="M1 1h12v7H5l-3 3V8H1z" fill="none" stroke="#aaa"/></svg>12 Comments</span></div>
  <p style="margin-top:8px">This is the studio's version of Lorem Ipsum. Proin gravida nibh vel velit auctor aliquet. .. <a>Read more »</a></p>
</div>
<div class="post" style="left:160px;top:1744px">
  <div class="meta"><span><svg width="14" height="14" viewBox="0 0 14 14"><rect x="1" y="2" width="12" height="11" fill="none" stroke="#aaa"/><path d="M1 5h12" stroke="#aaa"/></svg>15 Nov, 2012</span><span><svg width="14" height="12" viewBox="0 0 14 12"><path d="M1 1h12v7H5l-3 3V8H1z" fill="none" stroke="#aaa"/></svg>12 Comments</span></div>
  <p style="margin-top:8px">This is the studio's version of Lorem Ipsum. Proin gravida nibh vel velit auctor aliquet. .. <a>Read more »</a></p>
</div>

<div class="thumb thumb-news" style="left:484px;top:1634px" role="img" aria-label="Industrial site news photo"></div>
<div class="post" style="left:566px;top:1630px;width:160px">This is the studio's version of Lorem Ipsum. Proin gravida nibh vel velit aliquet. .. <a>Read more »</a></div>
<div class="thumb thumb-news" style="left:484px;top:1744px" role="img" aria-label="Industrial site news photo"></div>
<div class="post" style="left:566px;top:1740px;width:160px">This is the studio's version of Lorem Ipsum. Proin gravida nibh vel velit aliquet. .. <a>Read more »</a></div>

<div class="thumb thumb-client" style="left:806px;top:1634px" role="img" aria-label="Client portrait"></div>
<div class="post" style="left:888px;top:1630px;width:154px">"This is the studio's version of Lorem Ipsum. Proin gravida nibh vel velit<br><a>- Client Name</a></div>
<div class="thumb thumb-client" style="left:806px;top:1744px" role="img" aria-label="Client portrait"></div>
<div class="post" style="left:888px;top:1740px;width:154px">"This is the studio's version of Lorem Ipsum. Proin gravida nibh vel velit<br><a>- Client Name</a></div>

<footer class="site-footer">
  <div class="office" style="left:160px;top:50px">
    <h3>PERTH <em>Office</em></h3><div class="bar" style="background:var(--red)"></div>
    <p>Suite 4, 96 Kellaway Street Subiaco<br>Western Australia 6008</p>
    <p>Phone: +61 (08) 9517 3064<br>Email: perth@trivexpro.com.au</p>
  </div>
  <div class="office" style="left:482px;top:50px">
    <h3>BRISBANE <em>Office</em></h3><div class="bar" style="background:var(--orange)"></div>
    <p>Level 12, Marlowe Tower 118 Ferncliff<br>Street, Brisbane Queensland 4000</p>
    <p>Phone: +61 (07) 3421 6085<br>Email: brisbane@trivexpro.com.au</p>
  </div>
  <div class="office" style="left:160px;top:240px">
    <h3>HONG KONG <em>Office</em></h3><div class="bar" style="background:var(--cyan)"></div>
    <p>22/F Kestrel Centre 41 Lockmere Road<br>Wanchai, Hong Kong</p>
    <p>Phone: +852 8342 1176<br>Email: hongkong@trivexpro.asia</p>
  </div>
  <div class="office" style="left:482px;top:240px">
    <h3>SEOUL <em>Office</em></h3><div class="bar" style="background:var(--lime)"></div>
    <p>Level 18, Hanbit Tower 274 Seolleung-ro<br>Daechi dong, Gangnam-Gu Seoul, Republic of Korea</p>
    <p>Phone: +82 (0)2 6154 3390<br>Email: seoul@trivexpro.asia</p>
  </div>
</footer>
<div class="foot-title" style="top:1918px">JOIN OUR NEWSLETTER</div>
<div class="abs" style="left:806px;top:1950px;width:236px;font-size:13px;line-height:20px;color:var(--foot-text)">Enter your email to receive news &amp; updates.</div>
<div class="email-field">Enter your Email</div>
<div class="btn btn-blue" style="left:806px;top:2050px;width:94px;height:30px;line-height:30px;font-size:13px">SUBMIT</div>
<div class="foot-title" style="top:2104px">FOLLOW THE TRIVEX-PRO</div>
<div class="social">
  <span style="background:#3b5c9a"></span><span style="background:#29a8e0"></span><span style="background:#1a7bb8"></span><span style="background:#d6452f"></span><span style="background:#1aa0dc"></span><span style="background:#c9242a"></span>
</div>
<div class="foot-title" style="top:2196px">QUICK LINKS</div>
<div class="abs" style="left:806px;top:2228px;font-size:13px;line-height:22px;color:var(--foot-text)">Home | Job seekers | Employers<br>About us | News | Contact</div>

<div class="copy-bar">Copyright © 2013 Trivexpro.com.au All rights Reserved.</div>
<div class="to-top"><svg width="28" height="28" viewBox="0 0 28 28"><path d="M14 20V9M9 13l5-5 5 5" fill="none" stroke="#333" stroke-width="2"/></svg></div>

</body>
</html>
```